Grand Opening Banner needed for Marvelous Carpets and Home

My website is www.MarvelousCarpetsandHome.com (login with password 'plorka')

A full page banner 1000px X 500px with bright, lively colors and wording that shows an exciting GRAND OPENING celebration throughout the site. Banner needs to convey the following...

Grand Opening Sale
Runs through end of the month
Savings in every department
30 day Returns
Free Rug Pads with every rug
Free shipping.

Banner can be a simple background with graphics and text, or can be a room scene with rugs and furniture, or a grouping of rugs with text.

Some Ideas and Images can be taken from our vendor's websites, such as:

http://tbvendora.com/
http://dosmir.com/dosmir_2015/
http://www.pqmats.com/
http://zaverto.com/
http://shopbelwyn.com/

I also have quite a few room scene images available for use, if you desire.

Target Market(s)

Affluent women who care about stylish decor for their homes

Industry/Entity Type

Home And Garden

Requirements
Must have
• bold, vibrant appearance. Text that can be modified in Photoshop.
Nice to have
• HAND DRAWN, ARTIST STYLE ARTWORK IS GREATLY APPRECIATED.
• flat graphics and text with little to no 3 dimensional (shadow) effect. Font styles should be elegant/luxurious. An organic, scribbled, or painted style is nice in keeping with the handmade products that we sell.
• I am open to changing the color scheme of the website, to match your banner, so don't feel tied down to my existing colors.
Should not have
• nothing too modern or extreme in style.

```html
<!DOCTYPE html>
<html lang="en">
<head>
<meta charset="UTF-8">
<title>Grand Opening Sale</title>
<link rel="stylesheet" href="https://fonts.googleapis.com/css2?family=Josefin+Sans:wght@400;600&display=swap">
<style>
  :root {
    --wood-dark: #2b2019;
    --wood-mid: #4a3628;
    --rug-mustard: #b8892f;
    --rug-teal: #7fb2a8;
    --rug-rose: #b86a6a;
    --text-white: #ffffff;
    --text-peach: #f5c9a2;
  }
  * { margin: 0; padding: 0; box-sizing: border-box; }
  html, body {
    width: 1200px;
    height: 600px;
    overflow: hidden;
    background: var(--wood-dark);
  }
  .banner {
    position: relative;
    width: 1200px;
    height: 600px;
    overflow: hidden;
    font-family: "Josefin Sans", "Helvetica Neue", Arial, sans-serif;
    color: var(--text-white);
  }
  .banner__backdrop {
    position: absolute;
    inset: 0;
    background:
      radial-gradient(ellipse 55% 60% at 78% 72%, rgba(127,178,168,0.85), rgba(127,178,168,0) 70%),
      radial-gradient(ellipse 60% 55% at 45% 30%, rgba(184,137,47,0.9), rgba(184,137,47,0) 75%),
      linear-gradient(90deg, var(--wood-dark) 0%, var(--wood-mid) 14%, #6b4a2a 24%, var(--rug-mustard) 40%, #8f7a4e 60%, var(--rug-teal) 85%, #6a9a90 100%);
  }
  .banner__shade {
    position: absolute;
    inset: 0;
    background: rgba(30, 22, 16, 0.22);
  }
  .headline {
    position: absolute;
    top: 52px;
    left: 0;
    width: 1200px;
    text-align: center;
    font-size: 62px;
    font-weight: 400;
    letter-spacing: 0.3em;
    padding-left: 0.3em;
    line-height: 1;
  }
  .subline {
    position: absolute;
    top: 131px;
    left: 0;
    width: 1200px;
    text-align: center;
    font-size: 32px;
    font-weight: 400;
    letter-spacing: 0.3em;
    padding-left: 0.3em;
    color: var(--text-peach);
    line-height: 1;
  }
  .offers {
    position: absolute;
    left: 154px;
    top: 390px;
    width: 892px;
    height: 138px;
    border: 3px solid var(--text-white);
    display: flex;
    align-items: center;
  }
  .offers__item {
    text-transform: uppercase;
    letter-spacing: 0.2em;
    font-weight: 600;
  }
  .offers__savings {
    width: 286px;
    text-align: center;
    font-size: 18px;
    line-height: 1.4;
  }
  .offers__divider {
    width: 3px;
    height: 84px;
    background: var(--text-white);
  }
  .offers__returns {
    width: 300px;
    text-align: center;
  }
  .offers__returns-big {
    display: block;
    font-size: 70px;
    font-weight: 600;
    letter-spacing: 0.02em;
    line-height: 0.9;
  }
  .offers__returns-small {
    display: block;
    font-size: 21px;
    margin-top: 8px;
  }
  .offers__perks {
    padding-left: 32px;
    font-size: 16px;
    letter-spacing: 0.24em;
    line-height: 1.4;
  }
  .offers__perks p + p { margin-top: 14px; }
</style>
</head>
<body>
  <main class="banner">
    <div class="banner__backdrop" role="img" aria-label="Photo of two hand-tufted floral rugs, one mustard and one aqua, laid on a dark wooden floor"></div>
    <div class="banner__shade"></div>

    <h1 class="headline">GRAND OPENING SALE</h1>
    <p class="subline">RUNS THROUGH END OF THE MONTH</p>

    <section class="offers">
      <p class="offers__item offers__savings">Savings<br>in every<br>department</p>
      <span class="offers__divider"></span>
      <p class="offers__item offers__returns">
        <span class="offers__returns-big">30DAY</span>
        <span class="offers__returns-small">Returns</span>
      </p>
      <span class="offers__divider"></span>
      <div class="offers__item offers__perks">
        <p>Free rug pads<br>with every rug</p>
        <p>Free shipping</p>
      </div>
    </section>
  </main>
</body>
</html>
```